Business Card Layout and Stationary Layout
Business Card Layout and Stationary Layout -
Creative Brief
Use same font as used in my logo
CHANGE THE FONT TO SOMETHING NEW
Professional
Paul Dawson
P.O. Box 31842 Seattle WA 98173
Paul@Brintacor.com
Brintacor.com
We need a new font. Something where we can have BRINTACOR used just in font form. We love our logo, but we want a more creative high-powered, stand-alone font. We also need a letterhead layout and an invoice layout. Will pay winner an extra $50 for these two items.

```html
<!DOCTYPE html>
<html lang="en">
<head>
<meta charset="utf-8">
<title>Brintacor Stationery Concept</title>
<link href="https://fonts.googleapis.com/css2?family=Open+Sans:wght@400;700;800&display=swap" rel="stylesheet">
<style>
  :root {
    --bg-dark: #2b2d30;
    --bg-mid: #6a6d71;
    --brand-blue: #1f3f9a;
    --brand-navy: #0d1f5c;
    --band-light: #4f74d1;
    --paper: #ffffff;
    --paper-shade: #eef0f4;
    --ghost: #e3e6ec;
    --ink: #333a48;
    --label: #d9dbe0;
    --envelope-grey: #b9bcc2;
  }
  * { margin: 0; padding: 0; box-sizing: border-box; }
  html, body { width: 1200px; height: 427px; overflow: hidden; }
  body {
    font-family: "Open Sans", Arial, sans-serif;
    background: linear-gradient(180deg, var(--bg-dark) 0%, var(--bg-mid) 48%, var(--bg-dark) 100%);
    position: relative;
  }
  .wordmark { font-weight: 800; color: var(--brand-blue); letter-spacing: 0.2px; line-height: 1; }
  .mark-dot { display: inline-block; border-radius: 50%; background: var(--brand-blue); }

  /* intro */
  .intro { position: absolute; left: 40px; top: 88px; width: 150px; }
  .intro .mark-dot { width: 44px; height: 44px; display: block; margin: 0 0 8px 28px; }
  .intro .wordmark { color: #2b55c8; font-size: 24px; }
  .intro .subtitle { font-size: 9px; color: var(--label); margin-top: 3px; padding-left: 2px; }

  .label { position: absolute; font-size: 7px; color: var(--label); text-align: center; }

  /* business card */
  .business-card {
    position: absolute; left: 19px; top: 216px; width: 120px; height: 84px;
    background: var(--paper); border-radius: 5px; overflow: hidden;
    box-shadow: 0 2px 6px rgba(0,0,0,0.45);
  }
  .business-card .band {
    position: absolute; left: 0; top: 0; width: 100%; height: 26px;
    background: linear-gradient(90deg, var(--brand-navy), var(--band-light) 60%, var(--brand-navy));
  }
  .business-card .mark-dot { position: absolute; left: 50px; top: 12px; width: 20px; height: 20px; border: 2px solid #fff; }
  .business-card .wordmark { position: absolute; left: 0; width: 100%; top: 35px; text-align: center; font-size: 11px; }
  .business-card .person { position: absolute; left: 10px; top: 54px; font-size: 5px; color: var(--ink); line-height: 1.5; }
  .business-card .person b { font-size: 6px; color: var(--brand-blue); }
  .business-card .contact { position: absolute; right: 8px; top: 54px; font-size: 4.5px; color: var(--ink); line-height: 1.6; text-align: right; }

  /* letterheads */
  .letterhead {
    position: absolute; top: 24px; width: 212px; height: 379px;
    background: linear-gradient(180deg, var(--paper), var(--paper-shade));
    box-shadow: 0 2px 8px rgba(0,0,0,0.5);
  }
  .letterhead .band {
    position: absolute; left: 0; top: 16px; width: 100%; height: 16px;
    background: linear-gradient(90deg, var(--brand-navy), var(--brand-blue) 40%, var(--band-light) 75%, var(--brand-navy));
  }
  .letterhead .mark-dot { position: absolute; left: 94px; top: 9px; width: 24px; height: 24px; border: 2px solid #fff; }
  .letterhead .wordmark { position: absolute; left: 12px; top: 38px; font-size: 17px; }
  .letterhead .contact { position: absolute; right: 8px; top: 18px; font-size: 4px; color: #fff; line-height: 1.45; text-align: right; }
  .letterhead .ghost-circle {
    position: absolute; left: 22px; top: 90px; width: 168px; height: 168px; border-radius: 50%;
    background: radial-gradient(circle at 40% 35%, #f6f7fa, var(--ghost) 70%);
  }
  .letterhead .footer { position: absolute; left: 0; width: 100%; bottom: 14px; text-align: center; font-size: 3.6px; color: var(--ink); }
  .letterhead-one { left: 209px; }
  .letterhead-two { left: 439px; }

  .envelopes { position: absolute; left: 686px; top: 20px; }
  .envelopes text.wordmark-svg { font-family: "Open Sans", Arial, sans-serif; font-weight: 800; fill: var(--brand-blue); }
</style>
</head>
<body>

  <section class="intro">
    <span class="mark-dot"></span>
    <div class="wordmark">Brintacor</div>
    <div class="subtitle">Stationary Concept</div>
  </section>

  <article class="business-card">
    <div class="band"></div>
    <span class="mark-dot"></span>
    <div class="wordmark">Brintacor</div>
    <div class="person"><b>Paul Dawson</b><br>President</div>
    <div class="contact">Tel 206-555-0148<br>Paul@Brintacor.com<br>Brintacor.com</div>
  </article>
  <div class="label" style="left:19px; top:310px; width:120px;">Front side</div>

  <article class="letterhead letterhead-one">
    <div class="band"></div>
    <span class="mark-dot"></span>
    <div class="contact">P.O. Box 31842 Seattle WA 98173<br>Paul@Brintacor.com<br>Brintacor.com</div>
    <div class="wordmark">Brintacor</div>
    <div class="ghost-circle"></div>
  </article>
  <div class="label" style="left:209px; top:409px; width:212px;">Letterhead option 1</div>

  <article class="letterhead letterhead-two">
    <div class="band"></div>
    <span class="mark-dot"></span>
    <div class="contact">P.O. Box 31842 Seattle WA 98173<br>Paul@Brintacor.com<br>Brintacor.com</div>
    <div class="wordmark">Brintacor</div>
    <div class="ghost-circle"></div>
    <div class="footer">P.O. Box 31842 Seattle WA 98173 | Paul@Brintacor.com | Brintacor.com</div>
  </article>
  <div class="label" style="left:439px; top:409px; width:212px;">Letterhead option 2</div>

  <svg class="envelopes" width="290" height="385" viewBox="0 0 290 385" aria-label="Envelope set">
    <defs>
      <linearGradient id="blueBand" x1="0" x2="1">
        <stop offset="0" stop-color="#0d1f5c"/>
        <stop offset="0.45" stop-color="#1f3f9a"/>
        <stop offset="0.8" stop-color="#4f74d1"/>
        <stop offset="1" stop-color="#0d1f5c"/>
      </linearGradient>
      <linearGradient id="greyFlap" x1="0" y1="0" x2="0" y2="1">
        <stop offset="0" stop-color="#9fa3aa"/>
        <stop offset="1" stop-color="#d4d6da"/>
      </linearGradient>
    </defs>

    <!-- grey envelope back -->
    <g class="envelope-back-grey">
      <rect x="20" y="4" width="250" height="135" fill="#f2f3f5"/>
      <path d="M20 4 L145 70 L270 4 Z" fill="url(#greyFlap)"/>
      <path d="M20 139 L120 80 M270 139 L170 80" stroke="#c9ccd1" stroke-width="1" fill="none"/>
    </g>

    <!-- blue flap envelope -->
    <g class="envelope-back-blue">
      <rect x="4" y="82" width="274" height="100" fill="#f7f8fa"/>
      <path d="M4 82 L141 140 L278 82 Z" fill="url(#blueBand)"/>
      <path d="M4 182 L110 130 M278 182 L172 130" stroke="#d2d5db" stroke-width="1" fill="none"/>
    </g>

    <!-- white envelope back -->
    <g class="envelope-back-white">
      <rect x="14" y="178" width="252" height="90" fill="#ffffff"/>
      <path d="M14 178 L140 228 L266 178" stroke="#c9ccd1" stroke-width="1" fill="#f3f4f6"/>
      <path d="M14 268 L112 218 M266 268 L168 218" stroke="#d8dbe0" stroke-width="1" fill="none"/>
    </g>

    <!-- envelope front -->
    <g class="envelope-front">
      <rect x="4" y="268" width="236" height="106" fill="#ffffff"/>
      <rect x="4" y="274" width="236" height="16" fill="url(#blueBand)"/>
      <circle cx="205" cy="334" r="34" fill="#e6e9ef"/>
      <text class="wordmark-svg" x="12" y="311" font-size="16">Brintacor</text>
      <text x="12" y="321" font-size="4" fill="#333a48" font-family="Open Sans, Arial, sans-serif">P.O. Box 31842 Seattle WA 98173</text>
    </g>
  </svg>
  <div class="label" style="left:690px; top:409px; width:236px;">Envelope / Insert Back</div>

</body>
</html>
```